Gravonne Sela Vintra / Website

We are looking for a web design in modern baroque style for our launching on-line jewellery shop website. Through pitchmarket we have done a contest for the logo of our company, for which we have chosen the winner. See the files for the winning logo design.
Our on-line jewellery shop will sell hand made jewellery from an artist.

We will be building our site using the Pan Tilo Crest content management system.

In this contest we will need “Uncoded” files.
We expect to receive layered PSD files.
We will ask –outside this contest- a web development/designer to code it and bring it into a working web page.

The brand of our company is build around the following key words:
sophistication
smart looking
charming
nice-looking
feminine
smooth
stylish
fashionable
wearable
precious

The name of the company is Gravonne Sela Vintra, in brief GSV. We will use the website www.gravonne-sample.com. The logo will bear GVS and a mask as an insigne. The style of our brand is modern baroque.

The target group of the jewellery is Young Urban Professionals, people between 25 and 40 years old.

We want a dark background and a simple stylish background, in the style of modern baroque. This does not mean that the website should be crowded by curls, but it should contain baroque elements.

The basis idea about the website design is that it works like the user is opening jewellery boxes. By each click another inside world appears which provides some nice surprises.

The home page will contain a photo of a lady showing one of the pieces of jewellery (for this photo we plan to do a photoshooting once we have the design). And it will show the names of our 10 different collections. There will be no further information. One can click on each of the collection names to go to a specific collection page.

Each collection page (see the picture for an example of a collection) will show one big picture of a main feature of the jewelery, and it will show other elements of the collection in small pictures, like the:
necklace
earrings
bracelet
ring
complete set
We can not show the other jewellery yet, but for the design of the webpages you can use any pictures of jewellery, which we will definitely will not use for the final website.

Again by clicking on each of these small pictures another page appears showing the item in a similar designed web page.

And if appropriate there should be an option to choose between different color versions of the same set, which can go in maximum three different colors.

On each of the collection page there should be a rectangular frame, which looks like a jewellery box (see the picture for the style of the box we have chosen), with a further option to go to next pages in each corner. The name of each collection should be clearly written in the page.

The keywords for the buttons will be:
Origin
Buy
Ask
Become a fan

The “Origin” page will explain the background and history of the artist and the cultural heritage is refers to. This page has also to be designed in the same style as the other pages, but will read like a story in book which can contain different chapters:
- artist interview
- design origin
- cultural heritage
- preferred usage and tips
- etc.

The “Buy” page will provide the necessary elements to order the item. For this we will use a module of PanTiloCrest. The only thing needed for this page from a point of design is the background.

The “Ask” page will be on the possibility to send us an e-mail with questions. It will contain some items to be selected, but again for this page from a point of design the only thing needed for this page is the background.

The “Become a fan” page will contain the possibility to register yourself as a fan to get regular newsletters and updates by e-mail from GVS.

We like the following examples of other jewelery websites
www.vokr.ch
www.melbrinegems.com

The final result we will need are layered PSD files.
Updates

We have discussed in our team the technicalities of what we actually need in this contest.

What we will need is "Uncoded" files.
Outside this contest we will ask a web developer/designer to code it and to bring it into a working web page.

We have updated our brief accordingly.

Target Market(s)

Industry/Entity Type

It Company

Requirements
Must have
• The website should be really creative and be of another nature than informative websites. It should be a pleasure and a kind of discovery to go through our website.
Nice to have
• If the web site has moving elements, than it should drag you in from one page to another, like you are opening boxes.
Should not have
• The idea is that the website is not going crazy with pop ups and moving things, but is distinguished and a pleasure to look at.

```html
<!DOCTYPE html>
<html lang="en">
<head>
<meta charset="utf-8">
<title>GVS Gravonne – Origin</title>
<link rel="stylesheet" href="https://fonts.googleapis.com/css2?family=Lato:wght@300;400&display=swap">
<style>
  :root {
    --bg: #000000;
    --text: #d6d6d6;
    --text-soft: #bfbfbf;
    --heading: #cfcfcf;
    --divider: #3a3a3a;
    --frame: #f2f2f2;
    --glow: #5a5a5a;
    --logo: #c4c4c4;
    --hair-dark: #2a0f08;
    --hair-light: #9a4a26;
  }
  * { margin: 0; padding: 0; box-sizing: border-box; }
  html, body { width: 1200px; height: 900px; overflow: hidden; background: var(--bg); }
  body { font-family: "Lato", sans-serif; color: var(--text); position: relative; }

  .sidebar { position: absolute; left: 0; top: 0; width: 326px; height: 900px; }
  .sidebar-rule {
    position: absolute; left: 325px; top: 0; width: 1px; height: 900px;
    background: linear-gradient(to bottom, #1a1a1a, var(--divider) 30%, var(--divider) 70%, #1a1a1a);
  }

  .brand { position: absolute; left: 70px; top: 70px; color: var(--logo); font-weight: 300; }
  .brand-mark { display: block; font-size: 76px; letter-spacing: 6px; line-height: 1; }
  .brand-name { display: block; font-size: 17px; margin: 22px 0 0 44px; letter-spacing: 0.5px; }

  .main-nav { position: absolute; left: 0; top: 0; width: 326px; }
  .main-nav a {
    position: absolute; left: 115px; color: var(--text-soft); text-decoration: none;
    font-size: 16px; font-weight: 400; letter-spacing: 0.5px;
  }
  .main-nav .is-active { color: #e8e8e8; }
  .active-marker { position: absolute; left: 78px; top: 426px; width: 248px; height: 8px; }
  .active-marker .dot {
    position: absolute; left: 0; top: 1px; width: 6px; height: 6px; border-radius: 50%;
    background: #fff; box-shadow: 0 0 6px 3px rgba(255,255,255,0.7);
  }
  .active-marker .line {
    position: absolute; left: 4px; top: 4px; width: 244px; height: 1px;
    background: linear-gradient(to right, #ffffff, #eeeeee 38%, #555 42%, #3a3a3a);
  }
  .side-ornament {
    position: absolute; left: 60px; top: 715px; width: 265px; height: 70px;
    background: radial-gradient(ellipse at 60% 50%, rgba(80,80,80,0.45), rgba(0,0,0,0) 70%);
  }

  .top-band {
    position: absolute; left: 326px; top: 0; width: 874px; height: 223px;
    background:
      linear-gradient(to right, rgba(0,0,0,0) 60%, rgba(0,0,0,0.55)),
      linear-gradient(to bottom, #000 50%, #262626 80%, var(--glow) 100%);
  }
  .bottom-band {
    position: absolute; left: 326px; top: 703px; width: 874px; height: 110px;
    background:
      linear-gradient(to right, rgba(0,0,0,0) 55%, rgba(0,0,0,0.5)),
      linear-gradient(to bottom, #4a4a4a 0%, #1e1e1e 45%, #000 100%);
  }

  .story-box { position: absolute; left: 326px; top: 223px; width: 874px; height: 480px; background: var(--bg); }
  .story-frame { position: absolute; left: 0; top: 0; width: 3px; height: 480px; background: var(--frame); }
  .artist-photo {
    position: absolute; left: 3px; top: 0; width: 319px; height: 480px;
    background:
      radial-gradient(ellipse at 48% 22%, var(--hair-light), var(--hair-dark) 45%, rgba(0,0,0,0) 70%),
      linear-gradient(to bottom, #120806, #1a1a1e 60%, #0c0c10);
  }
  .story-ornament {
    position: absolute; left: 500px; top: 370px; width: 374px; height: 110px;
    background: radial-gradient(ellipse at 55% 60%, rgba(70,70,70,0.45), rgba(0,0,0,0) 70%);
  }

  .story-text { position: absolute; left: 362px; top: 18px; width: 410px; }
  .artist-name { font-size: 19px; font-weight: 400; color: var(--heading); letter-spacing: 0.3px; }
  .artist-role { font-size: 13px; color: var(--text-soft); margin-top: 3px; }
  .chapter { margin-top: 24px; }
  .chapter + .chapter { margin-top: 22px; }
  .chapter h2 { font-size: 12px; font-weight: 400; color: var(--text-soft); letter-spacing: 0.3px; margin-bottom: 3px; }
  .chapter p { font-size: 11.5px; line-height: 22px; color: var(--text); }

  .read-more {
    position: absolute; left: 376px; top: 424px; display: flex; align-items: center;
    color: var(--text-soft); text-decoration: none; font-size: 12px;
  }
  .read-more svg { margin-right: 12px; }

  .footer-nav a {
    position: absolute; top: 822px; font-size: 10.5px; color: var(--text-soft);
    text-decoration: none; letter-spacing: 0.3px;
  }
</style>
</head>
<body>
  <aside class="sidebar">
    <div class="brand">
      <span class="brand-mark">GVS</span>
      <span class="brand-name">Gravonne</span>
    </div>

    <nav class="main-nav">
      <a href="#" style="top:321px">HOME</a>
      <a href="#" class="is-active" style="top:405px">ORIGIN</a>
      <a href="#" style="top:490px">BUY</a>
      <a href="#" style="top:574px">ASK</a>
      <a href="#" style="top:658px">BECOME A FAN</a>
    </nav>
    <div class="active-marker"><span class="line"></span><span class="dot"></span></div>

    <div class="side-ornament" role="img" aria-label="Faint baroque scroll ornament"></div>
  </aside>
  <div class="sidebar-rule"></div>

  <div class="top-band"></div>

  <section class="story-box">
    <div class="artist-photo" role="img" aria-label="Photo of the artist with red hair wearing a black top and a statement necklace"></div>
    <div class="story-frame"></div>
    <div class="story-ornament" role="img" aria-label="Faint baroque scroll ornament"></div>

    <article class="story-text">
      <h1 class="artist-name">Mira Solenne</h1>
      <p class="artist-role">jewelry designer</p>

      <div class="chapter">
        <h2>ARTIST INTERVIEW</h2>
        <p>Its been ten years that she practices her craft in a small studio, shaping silver by hand and setting each stone with patience and a quiet love for old forms and new light, always finished and polished by her own two hands.</p>
      </div>
      <div class="chapter">
        <h2>DESIGN ORIGIN</h2>
        <p>Her designs might be read as small stories, each one drawn from lace, masks and old palace rooms, then made light enough to wear every day.</p>
      </div>
      <div class="chapter">
        <h2>CULTURAL HERITAGE</h2>
        <p>Venetian carnival masks and baroque scrollwork meet modern city life in every piece she makes.</p>
      </div>
    </article>

    <a href="#" class="read-more">
      <svg width="20" height="20" viewBox="0 0 20 20" aria-hidden="true" fill="#e0e0e0">
        <circle cx="3" cy="10" r="1.3"/><circle cx="7" cy="10" r="1.3"/><circle cx="11" cy="10" r="1.3"/><circle cx="15" cy="10" r="1.3"/>
        <circle cx="11" cy="6" r="1.3"/><circle cx="11" cy="14" r="1.3"/>
        <circle cx="9" cy="2" r="1.3"/><circle cx="9" cy="18" r="1.3"/>
        <circle cx="18.5" cy="10" r="1.3"/><circle cx="14" cy="6.5" r="1"/><circle cx="14" cy="13.5" r="1"/>
      </svg>
      Read More Artist
    </a>
  </section>

  <div class="bottom-band"></div>

  <nav class="footer-nav">
    <a href="#" style="left:356px">ABOUT US</a>
    <a href="#" style="left:483px">NEWS</a>
    <a href="#" style="left:609px">GALLERY</a>
    <a href="#" style="left:736px">WHOLESALE TRADE</a>
    <a href="#" style="left:905px">ARTICLES</a>
    <a href="#" style="left:1031px">CONTAC US</a>
  </nav>
</body>
</html>
```